依頼概要
■依頼の目的/概要
「ひなげし名品の会」は足利市内の26の店舗がそれぞれの良い所を伸ばそうとする「逸品運動」を中心に共同で事業を行う組織です。
栃木県足利市は国宝霞峰寺、日本遺産千草学舎などの重要な史跡が点在すところから東の京都、北の鎌倉などと言われることがあります。また、霧見川橋、スカイプラザ、森下はるおの故郷など観光などのポイントが多数あります。
※添付ファイルに会員のカタログがあります。

■依頼詳細
「ひなげし名品の会」加盟の店舗は市内の各所に点在しております。そのためそれぞれの店舗の店頭に飾れるような「のぼり旗」のデザインを募集します。
※添付ファイルに地図があります。

■重視する点
【必須項目】
「ひなげし名品の会」という文字表記

のぼり旗という制約のあるデザインの中で名品会らしさ、足利らしさなどを取り込んだものを希望します。通常ののぼり旗の概念を逸脱するものでも結構ですが、予算が必要以上にかかり様なアイデアは採用が難しくなる可能性がございます。

その他何かご不明な点がございましたら、お気軽にご質問下さい。
よろしくお願いいたします。
足利市のイメージキャラクターをのぼりデザインに使用する事は可能です。
ただし「ひなげし名品会」のイメージキャラクターではございませんのでご確認ください。
なお、キャラクター使用許諾につきましては当会にて行います。
添付データとして「まさとき君」のイラストレータデータを添付させていただきますのでこちらを使用願います。
(※当依頼以外でまさとき君の画像当を使用する場合は霜月観光協会の許可が必要ですのでご注意ください。)
名品の会全体会議にてデザインの選定を行う予定です。
そのため直前の3月14日まで受付を延長させていただきます。
より多くの提案をお願いしたいと思います。
■ 選んだ理由

名品の会の会員からのアンケート調査に基づいて決定いたしました。

■ 提案者全員のお礼・コメント

このたびは名品会ののぼりをデザイン頂き誠にありがとうございます。
市内の各所にこのデザインが掲載されお客様に親しまれるように頑張りたいと思います。

```html
<!DOCTYPE html>
<html lang="ja">
<head>
<meta charset="utf-8">
<title>ひなげし名品の会 のぼり旗</title>
<link rel="stylesheet" href="https://fonts.googleapis.com/css2?family=Yuji+Boku&family=Yuji+Syuku&display=swap">
<style>
  :root {
    --navy: #15175f;
    --navy-deep: #0c0d45;
    --brush-red: #a8121b;
    --brush-white: #f4f2ee;
    --wisteria-light: #d9d9dc;
    --wisteria-mid: #9a9aa6;
    --gold-light: #fff3c4;
    --gold: #e2b94c;
    --silver: #c8c8d2;
  }
  html, body {
    margin: 0;
    padding: 0;
    width: 1200px;
    height: 3592px;
    overflow: hidden;
    background: var(--navy);
  }
  .banner {
    position: relative;
    width: 1200px;
    height: 3592px;
    overflow: hidden;
    background: radial-gradient(ellipse at 60% 45%, var(--navy) 0%, var(--navy-deep) 100%);
  }
  .wisteria {
    position: absolute;
    left: 0;
    top: 0;
    width: 440px;
    height: 2380px;
    background: linear-gradient(180deg, var(--wisteria-light) 0%, var(--wisteria-mid) 70%, rgba(154,154,166,0) 100%);
    border-radius: 0 0 180px 40px;
    opacity: .85;
  }
  .gold-wave {
    position: absolute;
    left: 0;
    bottom: 0;
    width: 1200px;
    height: 1060px;
  }
  .title {
    position: absolute;
    inset: 0;
    font-family: "Yuji Boku", "Yuji Syuku", serif;
  }
  .title .place {
    position: absolute;
    left: 560px;
    top: 230px;
    font-family: "Yuji Syuku", serif;
    font-size: 150px;
    color: var(--brush-white);
    transform: rotate(-8deg);
    letter-spacing: 4px;
    white-space: nowrap;
  }
  .title .char {
    position: absolute;
    line-height: 1;
    white-space: nowrap;
  }
  .char-mei {
    left: 440px;
    top: 620px;
    font-size: 760px;
    color: var(--brush-red);
    transform: rotate(-4deg);
  }
  .char-hin {
    left: 620px;
    top: 1560px;
    font-size: 460px;
    color: var(--brush-white);
  }
  .char-no {
    left: 760px;
    top: 2200px;
    font-size: 330px;
    color: var(--brush-white);
  }
  .char-kai {
    left: 700px;
    top: 2640px;
    font-size: 420px;
    color: var(--brush-white);
  }
</style>
</head>
<body>
<div class="banner">
  <div class="wisteria" role="img" aria-label="白く垂れ下がる藤の花のイラスト"></div>

  <svg class="gold-wave" viewBox="0 0 1200 1060" role="img" aria-label="左下から流れる金と銀の波形装飾">
    <defs>
      <linearGradient id="goldFill" x1="0" y1="0" x2="1" y2="0">
        <stop offset="0" stop-color="var(--gold)"/>
        <stop offset=".45" stop-color="var(--gold-light)"/>
        <stop offset="1" stop-color="var(--gold)"/>
      </linearGradient>
      <radialGradient id="glow" cx=".3" cy="1" r=".8">
        <stop offset="0" stop-color="#ffffff" stop-opacity=".7"/>
        <stop offset="1" stop-color="#ffffff" stop-opacity="0"/>
      </radialGradient>
    </defs>
    <rect x="0" y="200" width="1200" height="860" fill="url(#glow)"/>
    <path d="M0 40 C120 60 160 160 260 180 C380 200 360 320 480 360 C600 400 580 520 700 580 C820 640 820 760 960 820 C1080 870 1140 980 1200 1060 L0 1060 Z" fill="var(--silver)"/>
    <path d="M0 110 C100 130 130 220 220 240 C330 265 320 380 430 420 C540 460 530 580 640 640 C750 700 760 820 880 880 C980 930 1030 1010 1060 1060 L0 1060 Z" fill="url(#goldFill)"/>
  </svg>

  <h1 class="title" aria-label="ひなげし名品の会">
    <span class="place">ひなげし</span>
    <span class="char char-mei">名</span>
    <span class="char char-hin">品</span>
    <span class="char char-no">の</span>
    <span class="char char-kai">会</span>
  </h1>
</div>
</body>
</html>
```